5 Planner Covers for Teacher Planners

Hello,
I currently run a Speech-Language Pathologist website and have created a planner for my fellow Speech Therapist. I would like someone to create 5 different planner covers so my followers will have different options to choose from.
Here is my planner from last year to give you an idea of what the planner will look like http://www.talkbloomshop.example/free-slp-planner/
My followers are mostly women aged 25-50. However, I don't want the covers to be overly girly or excessive with flowers. Simple is better.
I'd also like there to be an editable text box to allow the Speech Therapist to type their name on their cover if they wish.
Planner Cover can say any of the following: SLP Planner, Planner, Speech Therapy Planner, Speech-Language Pathologist (maybe this title could be editable as well??).
To give you an idea I have uploaded a screenshot of last year's planners cover that I made myself.
What I am looking for:
-Size 8.5" by 11"
-5 different planner covers
-1 gender-neutral cover
-simple design
-limited flowers (or overly girly
-text box to add a personal name
-Possible titles: SLP Planner, Planner, Speech Therapy Planner, Speech-Language Pathologist (maybe this title could be editable as well??)
Target Market(s)
Women aged 25-50
Colors
Designer to choose colors to be used in the design.
Requirements
Must have
- What I am looking for:
-Size 8.5" by 11"
-1 gender-neutral cover
-simple design
Nice to have
- I've uploaded some that I like from Craftora to give you an idea.
Here is my craftora store https://www.craftora.example/shop/QuietMeadowHome to give you an idea of things I like.
I like Marla Pendry and her simple elegant rustic style.

```html
<!DOCTYPE html>
<html lang="en">
<head>
<meta charset="utf-8">
<title>SLP Journal Cover</title>
<link rel="stylesheet" href="https://fonts.googleapis.com/css2?family=Montserrat:wght@500&display=swap">
<style>
  :root {
    --page-bg: #ffffff;
    --cover-pink: #ecc4be;
    --ink: #111111;
    --shadow: #6e6e6e;
    --marble-light: #f1e8e8;
    --marble-mid: #b9aaab;
  }
  * { margin: 0; padding: 0; box-sizing: border-box; }
  html, body {
    width: 1200px;
    height: 1200px;
    overflow: hidden;
    background: var(--page-bg);
  }
  .canvas {
    position: relative;
    width: 1200px;
    height: 1200px;
  }
  .cover {
    position: absolute;
    left: 300px;
    top: 180px;
    width: 600px;
    height: 840px;
    background: var(--cover-pink);
    box-shadow: 7px 7px 3px var(--shadow);
    overflow: hidden;
  }
  .cover-art {
    position: absolute;
    inset: 0;
    width: 600px;
    height: 840px;
  }
  .title-block {
    position: absolute;
    left: 0;
    right: 0;
    top: 165px;
    text-align: center;
    color: var(--ink);
    font-family: "Montserrat", Arial, sans-serif;
    font-weight: 500;
  }
  .title-main {
    display: block;
    font-size: 34px;
    line-height: 1.2;
  }
  .title-owner-label {
    display: block;
    font-size: 12px;
    line-height: 1.4;
    margin-top: 10px;
    letter-spacing: 1px;
  }
  .name-line {
    position: absolute;
    left: 223px;
    top: 304px;
    width: 154px;
    height: 1px;
    background: var(--ink);
    opacity: 0.75;
  }
</style>
</head>
<body>
<div class="canvas">
  <div class="cover">
    <svg class="cover-art" viewBox="0 0 600 840" xmlns="http://www.w3.org/2000/svg">
      <defs>
        <linearGradient id="gold-band" x1="0" y1="0" x2="600" y2="0" gradientUnits="userSpaceOnUse">
          <stop offset="0" stop-color="#c9a88e"/>
          <stop offset="0.12" stop-color="#f3d6b6"/>
          <stop offset="0.35" stop-color="#d2ad93"/>
          <stop offset="0.55" stop-color="#c4a08a"/>
          <stop offset="0.82" stop-color="#e3cfa4"/>
          <stop offset="1" stop-color="#b59d88"/>
        </linearGradient>
        <radialGradient id="marble-tone" cx="0.6" cy="0.65" r="0.7">
          <stop offset="0" stop-color="#b9aaab"/>
          <stop offset="0.5" stop-color="#d6cbcc"/>
          <stop offset="1" stop-color="#f1e8e8"/>
        </radialGradient>
      </defs>
      <polygon class="gold-band" points="0,728 600,360 600,468 0,840" fill="url(#gold-band)"/>
      <polygon class="marble-panel" role="img" aria-label="Grey and white marble texture" points="0,840 600,468 600,840" fill="url(#marble-tone)"/>
    </svg>

    <div class="title-block">
      <span class="title-main">SLP Journal</span>
      <span class="title-owner-label">Belongs to</span>
    </div>
    <div class="name-line"></div>
  </div>
</div>
</body>
</html>
```